ALL TEXT Social Media Graphics

We are looking for a series of social media graphics for Instagram (new size: 4:5 (1080 x 1350 pixels) ratio that are ALL TEXT. We want the following quotes below on each graphic; one quote per graphic. AND, In very small letters at the bottom of each graphic, add @PaulaWrenLive
The look and feel of these graphics should be complimentary to the color palette attached below; but keep them simple. But the design is up to you; at the end of this document, I provided various samples of all text graphics that I like as examples.
The Quotes are in the attached WORD document
women trying to lose weight

```html
<!DOCTYPE html>
<html lang="en">
<head>
<meta charset="utf-8">
<title>Summer Slimdown Quote</title>
<link rel="stylesheet" href="https://fonts.googleapis.com/css2?family=Fraunces:opsz,wght@9..144,400;9..144,700&family=Inter:wght@500&display=swap">
<style>
  :root {
    --berry: #ad1657;
    --blush: #f8e7ef;
    --white: #ffffff;
    --ink: #111111;
  }
  html, body {
    margin: 0;
    padding: 0;
    width: 960px;
    height: 1200px;
    overflow: hidden;
    background: var(--blush);
  }
  .quote-card {
    position: relative;
    width: 960px;
    height: 1200px;
    background: var(--blush);
  }
  .headline-band {
    position: absolute;
    left: 0;
    top: 0;
    width: 960px;
    height: 437px;
    background: var(--berry);
  }
  .headline,
  .promise,
  .call-to-action,
  .handle {
    position: absolute;
    left: 74px;
    margin: 0;
  }
  .headline {
    top: 99px;
    font-family: "Fraunces", Georgia, serif;
    font-weight: 700;
    font-size: 71px;
    line-height: 77px;
    letter-spacing: -0.5px;
    color: var(--white);
  }
  .promise {
    top: 486px;
    font-family: "Fraunces", Georgia, serif;
    font-weight: 700;
    font-size: 71px;
    line-height: 77px;
    letter-spacing: -0.5px;
    color: var(--berry);
  }
  .call-to-action {
    top: 798px;
    font-family: "Fraunces", Georgia, serif;
    font-weight: 400;
    font-size: 51px;
    line-height: 65px;
    color: var(--ink);
  }
  .handle {
    top: 1097px;
    font-family: "Inter", Arial, sans-serif;
    font-weight: 500;
    font-size: 27px;
    line-height: 34px;
    color: var(--berry);
  }
</style>
</head>
<body>
  <main class="quote-card">
    <div class="headline-band"></div>
    <h1 class="headline">You can absolutely<br>be down 20-30 pounds<br>by end of summer.</h1>
    <p class="promise">All it takes is<br>the right plan—and<br>you've found it.</p>
    <p class="call-to-action">Comment “Sunny”<br>for the Sunny<br>Summer Slimdown!</p>
    <p class="handle">@PaulaWrenLive</p>
  </main>
</body>
</html>
```